Brindle Structures Construction Company Seeking Modern Website

We are a small construction company wanting to create a web presence. We don't have much in the way of current content but will get photos as they come in. Attached is a picture of our business card.
The pages we would like on the menu are:
Home
Portfolio
Product Specs
Testimonials
Our Process
Contact
Some designs we like are:
http://www.tovenquarnsheds.example/
http://www.qzrsheds.example/
http://pannowsheds.example/
http://wistenhalls.example/
Not much requirements other than that so feel free to be creative!
Updates
Target Market(s)
Construction
Commercial and Residential Buildings
Industry/Entity Type
Construction Company
Number of Pages Required
5+ page
Look and feel

```html
<!DOCTYPE html>
<html lang="en">
<head>
<meta charset="utf-8">
<title>Brindle Structures Construction Company</title>
<link rel="stylesheet" href="https://fonts.googleapis.com/css2?family=PT+Sans:wght@400;700&display=swap">
<style>
:root{
  --green:#93b43a;
  --ink:#1e1e1e;
  --text:#2b2b2b;
  --muted:#8a8a8a;
  --line:#cfcfcf;
  --band:#222222;
  --footer:#1b1b1b;
  --footer-base:#0d0d0d;
  --white:#ffffff;
}
*{margin:0;padding:0;box-sizing:border-box}
html,body{width:1200px;height:3150px;overflow:hidden}
body{position:relative;background:var(--white);font-family:"PT Sans",sans-serif;color:var(--text)}
.abs{position:absolute}
.top-rule{left:0;top:0;width:1200px;height:10px;background:var(--ink)}
.social{right:70px;top:16px;display:flex;gap:10px}
.social span{width:20px;height:20px;background:var(--ink);display:block}
.search{left:970px;top:63px;width:195px;height:18px;background:#efefef;border:1px solid #e2e2e2}
.logo{left:0;width:1200px;top:38px;text-align:center;font-size:48px;letter-spacing:2px;color:var(--ink)}
.nav{top:150px;left:0;width:1200px;height:48px}
.nav a{position:absolute;top:0;font-size:22px;color:var(--ink);text-decoration:none}
.nav a.active::before{content:"";position:absolute;left:0;right:0;top:-22px;height:3px;background:var(--green)}
.hero{left:38px;top:246px;width:1124px;height:425px;background:linear-gradient(120deg,#9fb8cf 0%,#6f8aa5 40%,#c9a24b 62%,#4a5f74 100%);box-shadow:0 24px 26px -18px rgba(0,0,0,.55)}
.hero-caption{left:54px;top:396px;width:330px;color:var(--white)}
.hero-caption h2{font-size:32px;font-weight:400;margin-bottom:8px}
.hero-caption p{font-size:15px;line-height:20px}
.hero-caption a{display:block;margin-top:6px;font-size:15px;color:var(--green);text-decoration:none}
.dots{display:flex;gap:8px}
.dots i{width:10px;height:10px;border-radius:50%;background:#d8d8d8;display:block}
.dots i.on{background:var(--green)}
.lead{left:236px;width:728px;text-align:center;font-size:15px;line-height:24px;color:var(--text)}
.feature{top:898px;width:300px}
.feature .icon{width:138px;height:151px;border:2px solid #9a9a9a;background:#f1f1f1;display:flex;align-items:center;justify-content:center}
.feature .icon.current{border-color:var(--green)}
.feature .icon span{width:96px;height:96px;background:#7a7a7a;display:block}
.feature h3{margin-top:44px;font-size:34px;font-weight:700;color:#111}
.feature p{margin-top:14px;font-size:15px;line-height:23px;width:256px}
.btn{display:inline-block;width:151px;height:32px;border:1px solid var(--line);font-size:15px;line-height:30px;text-align:center;color:var(--text);text-decoration:none}
.feature .btn{margin-top:22px}
.band{left:47px;width:1106px;height:342px;background:var(--band);color:var(--white)}
.band .photo{position:absolute;top:0;height:100%}
.band h2{position:absolute;font-size:34px;font-weight:700}
.band p{position:absolute;font-size:15px;line-height:24px;width:260px}
.band .btn{position:absolute;border-color:#bdbdbd;color:var(--green)}
.band .dots{position:absolute}
.band .dots i{background:#bdbdbd}
.column{top:2362px;width:420px}
.column h3{font-size:34px;font-weight:700;line-height:40px;color:#111}
.column p{margin-top:24px;font-size:15px;line-height:24px}
.column .btn{margin-top:26px}
.footer{left:0;top:2756px;width:1200px;height:394px;background:var(--footer);color:var(--white)}
.footer h4{position:absolute;top:40px;font-size:32px;font-weight:400}
.footer ul{position:absolute;top:98px;list-style:none;font-size:15px;line-height:27px}
.footer li.current{color:var(--green)}
.footer p{position:absolute;top:98px;font-size:15px;line-height:24px}
.to-top{left:1096px;top:3049px}
.base{left:0;top:3112px;width:1200px;height:38px;background:var(--footer-base);color:var(--white);font-size:15px;line-height:38px;text-align:center}
</style>
</head>
<body>
<div class="abs top-rule"></div>
<div class="abs social" aria-label="Social links"><span></span><span></span><span></span><span></span></div>
<div class="abs logo">LOGO</div>
<div class="abs search" aria-label="Search"></div>

<nav class="abs nav">
  <a class="active" href="#" style="left:205px">Home</a>
  <a href="#" style="left:312px">Portfolio</a>
  <a href="#" style="left:438px">Product Specs</a>
  <a href="#" style="left:617px">Testimonials</a>
  <a href="#" style="left:781px">Our Process</a>
  <a href="#" style="left:929px">Contact</a>
</nav>

<div class="abs hero" role="img" aria-label="Photo of two construction workers in hard hats and safety vests reviewing plans at a steel-frame building site"></div>
<div class="abs hero-caption">
  <h2>Lorem Ipsum</h2>
  <p>It was popularised in the 1960s with the release of Letraset sheets containing</p>
  <a href="#">Read more</a>
</div>
<div class="abs dots" style="left:590px;top:625px"><i></i><i class="on"></i><i></i></div>

<p class="abs lead" style="top:770px">Lorem Ipsum has been the industry's standard dummy text ever since the 1500s, when an unknown printer took a galley of type and scrambled</p>

<section class="abs feature" style="left:117px">
  <div class="icon current" role="img" aria-label="Pictogram of recycling and construction materials"><span></span></div>
  <h3>Lorem Ipsum</h3>
  <p>Lorem Ipsum has been the industry's standard dummy text ever since the 1500s, when an unknown printer took a galley of type and scrambled</p>
  <a class="btn" href="#">Read more</a>
</section>
<section class="abs feature" style="left:504px">
  <div class="icon" role="img" aria-label="Pictogram of an arched doorway"><span></span></div>
  <h3>Lorem Ipsum</h3>
  <p>Lorem Ipsum has been the industry's standard dummy text ever since the 1500s, when an unknown printer took a galley of type and scrambled</p>
  <a class="btn" href="#">Read more</a>
</section>
<section class="abs feature" style="left:857px">
  <div class="icon" role="img" aria-label="Pictogram of industrial buildings"><span></span></div>
  <h3>Lorem Ipsum</h3>
  <p>Lorem Ipsum has been the industry's standard dummy text ever since the 1500s, when an unknown printer took a galley of type and scrambled</p>
  <a class="btn" href="#">Read more</a>
</section>

<section class="abs band" style="top:1361px">
  <h2 style="left:82px;top:46px">CONSTRUCTION</h2>
  <p style="left:82px;top:104px">Lorem Ipsum has been the industry's standard dummy text ever since the 1500s, when an unknown printer took a galley of type and scrambled</p>
  <a class="btn" href="#" style="left:82px;top:230px">Read more</a>
  <div class="photo" role="img" aria-label="Photo of a worker holding a yellow hard hat in front of a building under construction" style="left:561px;width:545px;background:linear-gradient(160deg,#5f8fc9 0%,#9ab9d8 45%,#c9c2a8 75%,#6d6a55 100%)"></div>
  <div class="dots" style="left:810px;top:320px"><i></i><i class="on"></i><i></i></div>
</section>

<p class="abs lead" style="top:1785px">Lorem Ipsum has been the industry's standard dummy text ever since the 1500s, when an unknown printer took a galley of type and scrambled</p>

<section class="abs band" style="top:1918px">
  <div class="photo" role="img" aria-label="Photo of a yellow hard hat, hammer and measuring tools on building plans" style="left:0;width:539px;background:linear-gradient(135deg,#d9c23a 0%,#bdbdb5 40%,#8e8e8a 70%,#c7c7c2 100%)"></div>
  <div class="dots" style="left:464px;top:322px"><i></i><i class="on"></i><i></i></div>
  <h2 style="left:637px;top:50px">QUALITY</h2>
  <p style="left:637px;top:108px">Lorem Ipsum has been the industry's standard dummy text ever since the 1500s, when an unknown printer took a galley of type and scrambled</p>
  <a class="btn" href="#" style="left:637px;top:227px">Read more</a>
</section>

<section class="abs column" style="left:117px">
  <h3>Lorem Ipsum has been the industry's</h3>
  <p>Lorem Ipsum has been the industry's standard dummy text ever since the 1500s, when an unknown printer took a galley of type and scrambled it to make a type specimen book. It has survived not only five centuries, but also the leap into electronic typesetting, remaining essentially unchanged</p>
  <a class="btn" href="#">Read more</a>
</section>
<section class="abs column" style="left:702px">
  <h3>Lorem Ipsum has been the industry's</h3>
  <p>Lorem Ipsum has been the industry's standard dummy text ever since the 1500s, when an unknown printer took a galley of type and scrambled it to make a type specimen book. It has survived not only five centuries, but also the leap into electronic typesetting, remaining essentially unchanged</p>
  <a class="btn" href="#">Read more</a>
</section>

<footer class="abs footer">
  <h4 style="left:47px">Menu</h4>
  <ul style="left:47px">
    <li class="current">Home</li>
    <li>Portfolio</li>
    <li>Product</li>
    <li>Specs</li>
    <li>Testimonials</li>
    <li>Our Process</li>
    <li>Contact</li>
  </ul>
  <h4 style="left:315px">Our Address</h4>
  <p style="left:315px;width:340px">Lorem Ipsum has been the industry's standard dummy text ever since the 1500s,</p>
  <h4 style="left:718px">Contact Info</h4>
  <p style="left:718px">Phone: 555-014.2270<br>Fax: 555.019.4410</p>
</footer>
<svg class="abs to-top" width="54" height="32" viewBox="0 0 54 32" aria-label="Back to top"><polygon points="27,0 54,32 0,32" fill="#ffffff"/></svg>
<div class="abs base">© 2015 Brindle Structures. All Rights Reserved</div>
</body>
</html>
```